Carpentry and Building Business Card

I'm looking for a business card that is minimalistic and that incorporates the theme of my Velmor logo.
On one side I'd like the VELMOR logo with my details on the other side.
Double sided with curved edges

Target Market(s)

Construction / renovation
Adults

Industry/Entity Type

Tradesman

Contact Information for Business Card

Logo on one side, details on the other

Colors

Designer to choose only greyscale colors for use in the design.

Requirements
Must have
• Nilo Petrakis
VELMOR CONSTRUCT
Carpentry & Building Services
0481236574
Velmorconstruct@brixmail.com
Lic No. 718263D
Nice to have
• Fb and insta icons. @velmorconstruct
Should not have
• No hammer or tool icons please.

No address line.

```html
<!DOCTYPE html>
<html lang="en">
<head>
<meta charset="utf-8">
<title>Velmor Construct – Business Card</title>
<link rel="stylesheet" href="https://fonts.googleapis.com/css2?family=Red+Hat+Display:wght@400;500;700&display=swap">
<style>
  :root {
    --backdrop: #e3e3e3;
    --card-dark: #212121;
    --card-light: #f4f4f4;
    --ink: #222222;
    --ink-soft: #333333;
    --white: #ffffff;
    --accent: #e8943a;
  }
  * { box-sizing: border-box; margin: 0; padding: 0; }
  html, body {
    width: 1200px;
    height: 960px;
    overflow: hidden;
    background: var(--backdrop);
    font-family: "Red Hat Display", sans-serif;
    color: var(--ink);
  }
  .canvas { position: relative; width: 1200px; height: 960px; }

  .card {
    position: absolute;
    left: 304px;
    width: 602px;
    height: 344px;
  }
  .card--front { top: 117px; background: var(--card-dark); }
  .card--back  { top: 515px; background: var(--card-light); }

  /* Front */
  .front-brand {
    position: absolute;
    left: 0; right: 0; top: 0; bottom: 0;
    display: flex;
    align-items: center;
    justify-content: center;
    gap: 26px;
  }
  .brand-square {
    width: 80px; height: 80px;
    border: 3px solid var(--accent);
  }
  .front-wordmark {
    font-size: 46px;
    font-weight: 500;
    letter-spacing: 0.2em;
    color: var(--white);
    line-height: 1;
  }

  /* Back */
  .back-wordmark {
    position: absolute;
    left: 49px; top: 40px;
    font-size: 34px;
    font-weight: 500;
    letter-spacing: 0.2em;
    color: var(--ink);
    line-height: 1;
  }
  .person { position: absolute; left: 50px; top: 120px; }
  .person-name {
    font-size: 20px;
    font-weight: 500;
    color: var(--accent);
    line-height: 26px;
  }
  .person-role { font-size: 16px; color: var(--ink-soft); line-height: 20px; }
  .divider {
    position: absolute;
    left: 50px; top: 176px;
    width: 36px; height: 2px;
    background: var(--accent);
  }
  .business { position: absolute; left: 50px; top: 196px; font-size: 16px; line-height: 21px; color: var(--ink-soft); }
  .business-name { font-weight: 700; color: var(--ink); }
  .business strong { font-weight: 700; color: var(--ink); }
  .contacts { position: absolute; left: 50px; top: 266px; font-size: 16px; line-height: 21px; color: var(--ink-soft); }
  .contact-row { display: flex; align-items: center; gap: 7px; }
  .contact-row svg { width: 14px; height: 14px; flex: none; }

  .back-mark {
    position: absolute;
    left: 438px; top: 52px;
    width: 118px; height: 118px;
    border: 3px solid var(--accent);
  }
  .social {
    position: absolute;
    right: 42px; top: 266px;
    width: 140px;
    text-align: center;
    font-size: 16px;
    line-height: 21px;
    color: var(--ink-soft);
  }
  .social-dot {
    display: block;
    width: 14px; height: 14px;
    margin: 3px auto 4px;
    border-radius: 50%;
    background: var(--accent);
  }
</style>
</head>
<body>
<main class="canvas">

  <section class="card card--front" aria-label="Card front">
    <div class="front-brand">
      <span class="brand-square" aria-hidden="true"></span>
      <span class="front-wordmark">VELMOR.</span>
    </div>
  </section>

  <section class="card card--back" aria-label="Card back">
    <div class="back-wordmark">VELMOR.</div>

    <div class="person">
      <p class="person-name">Nilo Petrakis</p>
      <p class="person-role">Founder</p>
    </div>
    <span class="divider" aria-hidden="true"></span>

    <div class="business">
      <p class="business-name">VELMOR CONSTRUCT</p>
      <p>Carpentry &amp; Building Services</p>
      <p><strong>Lic No.</strong> 718263D</p>
    </div>

    <div class="contacts">
      <p class="contact-row">
        <svg viewBox="0 0 24 24" aria-hidden="true"><path fill="#e8943a" d="M6.6 10.8c1.4 2.8 3.8 5.1 6.6 6.6l2.2-2.2c.3-.3.7-.4 1-.2 1.1.4 2.3.6 3.6.6.6 0 1 .4 1 1V20c0 .6-.4 1-1 1C10.6 21 3 13.4 3 4c0-.6.4-1 1-1h3.5c.6 0 1 .4 1 1 0 1.3.2 2.5.6 3.6.1.3 0 .7-.2 1z"/></svg>
        <span>0481236574</span>
      </p>
      <p class="contact-row">
        <svg viewBox="0 0 24 24" aria-hidden="true"><rect x="3" y="6" width="18" height="12" fill="none" stroke="#e8943a" stroke-width="2"/><path d="M3 6l9 7 9-7" fill="none" stroke="#e8943a" stroke-width="2"/></svg>
        <span>Velmorconstruct@brixmail.com</span>
      </p>
    </div>

    <span class="back-mark" aria-hidden="true"></span>

    <div class="social">
      <span class="social-dot" aria-hidden="true"></span>
      <span>@velmorconstruct</span>
    </div>
  </section>

</main>
</body>
</html>
```